IRON MESA TRAINING- Shooting Range!!!And virtual shooting range!!!

We are looking to do a clean cut web page for shooting range. We have indoor shooting simulator, retail store that sales accessories and pistols, rifles and shot guns. We are membership based for indoor shooting range Only and virtual shooting is open to public as well as retail store. We also specialize in shooting training classes and CWP classes.
Updates

Thank you for your patience. We are working with a busy travel schedule. We will be making final decisions tomorrow and moving forward with getting this launched. Regards, Harold

Target Market(s)

Public and private entertainment

Industry/Entity Type

Training

Number of Pages Required

5+ page

Font styles to use
Sans Serif

Requirements
Must have
• Clean and easy approach we really like the website our friend has www.vellorcrest.com please take a look at a lay out. We would like to also add onli member schedule that is available for shooting sections and that they can access and book them selvs.
Nice to have
• White, black, gray or red colors

```html
<!DOCTYPE html>
<html lang="en">
<head>
<meta charset="utf-8">
<title>Iron Mesa Training</title>
<link href="https://fonts.googleapis.com/css2?family=Open+Sans:wght@400;600;700;800&display=swap" rel="stylesheet">
<style>
:root{
  --red:#c4111f;
  --red-dark:#a10d19;
  --ink:#111;
  --text:#444;
  --yellow:#f5c400;
  --dark:#2b2b2b;
  --footer:#1f1f1f;
  --panel-top:#d3d8dd;
  --panel-bottom:#9aa1a8;
}
*{margin:0;padding:0;box-sizing:border-box}
html,body{width:1037px;height:1200px;overflow:hidden;background:#fff;font-family:"Open Sans",Arial,sans-serif}
.page{position:relative;width:1037px;height:1200px;border-top:3px solid var(--red)}
.abs{position:absolute}
.brand{left:52px;top:70px;display:flex;align-items:center;gap:10px}
.brand-dot{width:34px;height:34px;border-radius:50%;background:var(--red)}
.brand-name{font-size:19px;font-weight:800;color:#6d7278;letter-spacing:.5px;line-height:1.1;width:130px}
.phone{right:50px;top:36px;display:flex;align-items:center;gap:8px;color:var(--red);font-size:27px}
.phone svg{width:26px;height:26px}
.nav{left:466px;top:120px;display:flex;height:72px}
.nav a{display:block;color:#333;text-decoration:none;font-size:15px;padding:15px 15px 0;margin-right:16px}
.nav a.active{background:linear-gradient(var(--red),var(--red-dark));color:#fff;margin-right:16px;border-radius:3px 3px 0 0}
.hero{left:0;top:192px;width:1037px;height:496px;background:linear-gradient(#c8101e,#b50e1b 80%,#a30c18)}
.hero-frame{left:52px;top:46px;width:933px;height:397px;background:#fff;box-shadow:0 22px 30px rgba(80,0,0,.45)}
.slide{left:8px;top:8px;width:649px;height:381px;background:var(--dark);overflow:hidden}
.slide-photo{left:0;top:0;width:400px;height:381px;background:linear-gradient(90deg,#556b3a 0%,#4a5a36 45%,#3a3c36 75%,var(--dark) 100%)}
.slide-copy{left:312px;top:128px;width:320px;color:#fff}
.slide-kicker{font-size:18px;letter-spacing:.5px}
.slide-title{font-size:28px;font-weight:700;color:var(--yellow);margin-top:10px;letter-spacing:.5px}
.slide-text{font-size:11.5px;margin-top:8px;line-height:16px;color:#ddd}
.btn{display:inline-block;background:linear-gradient(#d11826,var(--red-dark));color:#fff;font-size:12px;font-weight:600;padding:8px 9px;border-radius:3px;box-shadow:0 2px 3px rgba(0,0,0,.35)}
.slide-copy .btn{margin-top:24px}
.dots{display:flex;gap:12px;margin-top:22px;margin-left:2px}
.dots span{width:12px;height:12px;border-radius:50%;background:#444}
.dots span.on{background:var(--red)}
.booking{left:665px;top:8px;width:260px;height:381px;background:linear-gradient(var(--panel-top),var(--panel-bottom));padding:24px 14px 0}
.booking h2{color:var(--red-dark);font-size:19px;font-weight:700;letter-spacing:.5px}
.booking label{display:block;font-size:14px;color:#222;margin:10px 0 5px 1px}
.booking .field{height:36px;background:#fff}
.booking .btn{margin-top:12px}
.feature{top:720px;width:291px}
.feature h3{font-size:29px;font-weight:800;color:var(--ink);letter-spacing:1px;margin-left:2px}
.feature-img{margin-top:20px;height:146px;box-shadow:0 14px 14px -10px rgba(0,0,0,.35)}
.feature p{font-size:12px;color:var(--text);line-height:19px;margin-top:24px}
.feature .btn{margin-top:30px}
.footer{left:0;top:1114px;width:1037px;height:86px;background:var(--footer);color:#9a9a9a;font-size:12px}
.footer-links{left:52px;top:23px;word-spacing:2px}
.footer-copy{left:52px;top:44px}
.social{right:53px;top:24px;display:flex;gap:6px}
.social span{width:29px;height:29px;background:#2c2c2c}
</style>
</head>
<body>
<div class="page">
  <div class="abs brand"><span class="brand-dot"></span><span class="brand-name">IRON MESA TRAINING</span></div>
  <div class="abs phone">
    <svg viewBox="0 0 26 26"><rect width="26" height="26" rx="4" fill="#c4111f"/><path d="M8 6c1-.6 2 .2 2.6 1.5l.8 1.8c.3.8-.2 1.4-.9 2 .8 1.8 2.2 3.3 4 4.1.6-.7 1.2-1.2 2-.9l1.8.8c1.3.6 2 1.6 1.5 2.6-.8 1.6-2.4 2.4-4.2 1.8C11.5 18.4 7.6 14.5 6.3 10.4 5.7 8.6 6.4 6.8 8 6z" fill="#fff"/></svg>
    1800-555-0142
  </div>
  <nav class="abs nav">
    <a class="active" href="#">HOME</a><a href="#">ABOUT US</a><a href="#">CLASSES</a><a href="#">NEWS</a><a href="#" style="margin-right:0">CONTACT US</a>
  </nav>

  <section class="abs hero">
    <div class="abs hero-frame">
      <div class="abs slide">
        <div class="abs slide-photo" role="img" aria-label="Trainee in camouflage aiming a rifle at an indoor range"></div>
        <div class="abs slide-copy">
          <div class="slide-kicker">SPECIALISE IN</div>
          <div class="slide-title">SHOOTING TRAINING</div>
          <div class="slide-text">Neque porro quisquam est qui dolorem ipsum quia dolor sit amet, consectetur, adipisci velit...</div>
          <span class="btn">READ MORE</span>
          <div class="dots"><span class="on"></span><span></span><span></span></div>
        </div>
      </div>
      <form class="abs booking">
        <h2>MEMBER BOOKINGS</h2>
        <label>Enter Your Name</label><div class="field"></div>
        <label>Enter Your Email</label><div class="field"></div>
        <label>Enter Your Phone Number</label><div class="field"></div>
        <label>Enter Your Phone Number</label><div class="field"></div>
        <span class="btn">BOOK NOW</span>
      </form>
    </div>
  </section>

  <article class="abs feature" style="left:52px">
    <h3>TRAINING</h3>
    <div class="feature-img" role="img" aria-label="Instructor in helmet aiming a pistol" style="background:linear-gradient(90deg,#5a5a5a,#2e2e2e 60%,#4a4a4a)"></div>
    <p>Nemo enim ipsam voluptatem quia voluptas sit aspernatur aut odit aut fugit, sed quia consequuntur magni dolores eos qui ratione</p>
    <span class="btn">READ MORE</span>
  </article>
  <article class="abs feature" style="left:373px">
    <h3>CLUB</h3>
    <div class="feature-img" role="img" aria-label="Club meeting room with a long table" style="background:linear-gradient(90deg,#c9c2b6 0%,#8a847a 20%,#151515 35%,#111 100%)"></div>
    <p>Nemo enim ipsam voluptatem quia voluptas sit aspernatur aut odit aut fugit, sed quia consequuntur magni dolores eos qui ratione</p>
    <span class="btn">READ MORE</span>
  </article>
  <article class="abs feature" style="left:694px">
    <h3>MEMBERS</h3>
    <div class="feature-img" role="img" aria-label="Rifles and pistols displayed on a pegboard wall" style="background:linear-gradient(#9a958c,#6c6862 60%,#3f3d3a)"></div>
    <p>Nemo enim ipsam voluptatem quia voluptas sit aspernatur aut odit aut fugit, sed quia consequuntur magni dolores eos qui ratione</p>
    <span class="btn">READ MORE</span>
  </article>

  <footer class="abs footer">
    <div class="abs footer-links">Home &nbsp;/&nbsp; About us /&nbsp; Classes &nbsp;/&nbsp; News &nbsp;/&nbsp; Contact us</div>
    <div class="abs footer-copy">©2015 Iron Mesa. All rights reserved.</div>
    <div class="abs social"><span></span><span></span><span></span><span></span><span></span></div>
  </footer>
</div>
</body>
</html>
```